Meadowlark in a league of it's own

Meadowlark is a pan European contact center.
We serve our clients in 18 languages from Antwerp in Belgium, Fez in Morocco and with our partner Vellorix.
We have a presentation and we would like to make it much more visible;
Less text, more images or animation.
Our business case is based on three elements with three colours :
blue sky : because we ar fully organized in the cloud,
Green : in our customer care college, out green village we put a lot of energy in training,
Orange : when technology is good and people have a good knowledge, passion will come...
Eventually we are ready to payfor some stock images - to negotiate-
For answers to your questions : tom.ravelin@brinkmail.be

```html
<!DOCTYPE html>
<html lang="en">
<head>
<meta charset="utf-8">
<title>Meadowlark – Presentation Slides</title>
<link href="https://fonts.googleapis.com/css2?family=Open+Sans:ital,wght@0,300;0,400;0,600;0,700;1,400;1,600&display=swap" rel="stylesheet">
<style>
:root{
  --board:#cdced0;
  --navy:#232b3c;
  --blue:#1b9ad7;
  --green:#8cba3a;
  --orange:#eb5a2b;
  --text:#8a8d92;
  --white:#ffffff;
}
*{margin:0;padding:0;box-sizing:border-box}
html,body{width:1200px;height:900px;overflow:hidden;background:var(--board);font-family:"Open Sans",sans-serif}
.board{position:relative;width:1200px;height:900px}
.slide{position:absolute;width:357px;height:276px;background:var(--white);overflow:hidden}
.slide::after{content:"";position:absolute;left:0;right:0;bottom:0;height:6px;background:var(--navy)}
.page-no{position:absolute;right:4px;bottom:0;font-size:3px;color:#fff;z-index:2;line-height:6px}
.s1{left:51px;top:192px}.s2{left:421px;top:192px}.s3{left:787px;top:192px}
.s4{left:51px;top:478px}.s5{left:421px;top:478px}.s6{left:787px;top:478px}

.slide-title{position:absolute;left:14px;top:14px;font-weight:300;font-size:13px;color:var(--blue);letter-spacing:-.2px}
.rule{position:absolute;left:14px;top:29px;width:330px;height:1.5px;
  background:linear-gradient(90deg,var(--orange) 0 33.3%,var(--green) 33.3% 66.6%,var(--blue) 66.6%)}
.brand{position:absolute;left:8px;bottom:12px;display:flex;align-items:center;gap:2px;font-weight:600;font-size:7.5px;color:var(--navy)}
.brand .dot{width:8px;height:8px;border-radius:50%;background:var(--green)}
.body-copy{font-weight:300;font-size:5px;line-height:9.5px;color:var(--text);text-align:justify}

/* cover */
.cover-panel{position:absolute;left:5px;top:5px;width:347px;height:159px;background:var(--navy)}
.cover-stripe{position:absolute;left:5px;top:164px;width:347px;height:3px;
  background:linear-gradient(90deg,var(--blue) 0 32%,var(--green) 32% 67%,var(--orange) 67%)}
.cover-title{position:absolute;right:29px;top:73px;text-align:right;color:#fff;font-weight:300;font-size:16px;line-height:22px;letter-spacing:-.3px}
.cover-date{position:absolute;right:29px;top:119px;color:#c6cad3;font-size:7.5px;font-weight:300}
.cover-brand{position:absolute;right:18px;top:204px;display:flex;align-items:center;gap:5px;font-weight:600;font-size:17px;color:var(--navy)}
.cover-brand .dot{width:20px;height:20px;border-radius:50%;background:var(--green)}

/* about */
.photo{position:absolute;background:linear-gradient(90deg,#9da0a4,#d9dadc 40%,#aeb1b4 70%,#e4e5e6)}
.about-photo{left:14px;top:38px;width:329px;height:75px}
.about-lead{position:absolute;left:14px;top:127px;width:105px;font-size:5.3px;line-height:9.2px;color:var(--blue)}
.about-copy{position:absolute;left:132px;top:126px;width:206px}
.about-copy p+p{margin-top:10px}
.about-band{position:absolute;left:0;right:0;top:61px;height:74px;background:var(--navy)}
.about-photo2{left:14px;top:48px;width:131px;height:88px;background:linear-gradient(90deg,#e6e7e8,#b8babd 60%,#d3d4d6)}
.about-quote{position:absolute;left:161px;top:73px;width:186px;color:#fff;font-style:italic;font-weight:600;font-size:5.5px;line-height:12.5px;text-align:justify}
.about-copy2{position:absolute;left:161px;top:144px;width:186px;line-height:12.6px}

/* team */
.team-intro{position:absolute;left:0;right:0;top:59px;text-align:center;font-style:italic;font-weight:600;font-size:4.8px;line-height:10px;color:#6e7176}
.member{position:absolute;top:92px;width:90px;text-align:center}
.member .avatar{width:52px;height:52px;margin:0 auto;border-radius:50%;border:1px solid var(--blue);background:radial-gradient(circle at 50% 40%,#d6d7d9,#8e9195)}
.member h3{margin-top:11px;font-weight:400;font-size:6px;color:var(--blue)}
.member .role{font-style:italic;font-size:4.5px;color:#555}
.member .body-copy{margin-top:6px;text-align:justify}
.m1{left:35px}.m2{left:138px}.m3{left:238px}

/* services */
.service{position:absolute;top:92px;width:100px;text-align:center}
.service .icon{width:44px;height:44px;border-radius:50%;margin:0 auto;display:flex;align-items:center;justify-content:center}
.service h3{margin-top:16px;font-weight:700;font-size:8px;color:var(--blue)}
.service .body-copy{margin-top:3px;text-align:center;line-height:7px;font-size:4.6px}
.sv1{left:16px}.sv2{left:121px}.sv3{left:236px}

/* bullets */
.bullets{position:absolute;left:50px;top:80px;width:294px;list-style:none}
.bullets li{position:relative;padding-left:8px;line-height:12.6px}
.bullets li+li{margin-top:27px}
.bullets li::before{content:"";position:absolute;left:0;top:4px;width:4px;height:4px;border-radius:50%;background:var(--green)}
</style>
</head>
<body>
<main class="board">

  <section class="slide s1">
    <div class="cover-panel"></div>
    <div class="cover-stripe"></div>
    <h1 class="cover-title">WELCOME<br>TO OUR PRESENTATION</h1>
    <p class="cover-date">Birmingham, March 25, 2014</p>
    <div class="cover-brand"><span class="dot"></span>meadowlark</div>
  </section>

  <section class="slide s2">
    <h2 class="slide-title">ABOUT US</h2><div class="rule"></div>
    <div class="photo about-photo" role="img" aria-label="Customer care agents wearing headsets"></div>
    <p class="about-lead">WE SERVE CLIENTS ACROSS EUROPE IN EIGHTEEN LANGUAGES FROM THREE CONNECTED CONTACT CENTRES</p>
    <div class="about-copy body-copy">
      <p>Our teams in Antwerp and Fez work together with our partner Vellorix to answer every call, email and chat with care. Fully organised in the cloud, we scale quickly and keep service steady for every client we support across many markets.</p>
      <p>Training comes first in our customer care college. When technology is good and people know their craft, passion follows and clients notice the difference every day in every conversation.</p>
    </div>
    <div class="brand"><span class="dot"></span>meadowlark</div>
    <span class="page-no">2</span>
  </section>

  <section class="slide s3">
    <h2 class="slide-title">ABOUT US</h2><div class="rule"></div>
    <div class="about-band"></div>
    <div class="photo about-photo2" role="img" aria-label="Smiling agent with headset in a contact centre"></div>
    <p class="about-quote">A pan European contact centre<br>serving clients in eighteen languages from Antwerp, Fez and with our partner network across the region, fully organised in the cloud and trained with care</p>
    <p class="about-copy2 body-copy">We are fully organised in the cloud, so our people can focus on what matters most. In our green village we put energy into training, coaching and growth. When tools work well and knowledge is strong, passion comes naturally. That is how we deliver care that clients trust, in every language, every day, with a team that stays curious and keeps learning together.</p>
    <div class="brand"><span class="dot"></span>meadowlark</div>
    <span class="page-no">2</span>
  </section>

  <section class="slide s4">
    <h2 class="slide-title">OUR TEAM</h2><div class="rule"></div>
    <p class="team-intro">People who lead our teams with care, energy and a clear focus on the customer in every language.<br>They guide our centres every day and keep training at the heart of all we do.</p>
    <div class="member m1">
      <div class="avatar" role="img" aria-label="Portrait of Jonathan Doe"></div>
      <h3>JONATHAN DOE</h3><p class="role">President</p>
      <p class="body-copy">Leads strategy and growth across our centres and keeps our clients close to every decision we make together.</p>
    </div>
    <div class="member m2">
      <div class="avatar" role="img" aria-label="Portrait of Melanie Doe"></div>
      <h3>MELANIE DOE</h3><p class="role">CEO / Founder</p>
      <p class="body-copy">Founded the company with a belief that trained, happy people give the best service to every caller.</p>
    </div>
    <div class="member m3">
      <div class="avatar" role="img" aria-label="Portrait of Natalie Doe"></div>
      <h3>NATALIE DOE</h3><p class="role">Vice President</p>
      <p class="body-copy">Runs daily operations and our customer care college, making sure each agent grows with skill and confidence.</p>
    </div>
    <div class="brand"><span class="dot"></span>meadowlark</div>
    <span class="page-no">2</span>
  </section>

  <section class="slide s5">
    <h2 class="slide-title">OUR SERVICES</h2><div class="rule"></div>
    <div class="service sv1">
      <div class="icon" style="background:var(--blue)">
        <svg width="26" height="16" viewBox="0 0 26 16" fill="none" stroke="#fff" stroke-width="3"><circle cx="7" cy="9" r="4.5"/><circle cx="19" cy="9" r="4.5"/><path d="M11 7h4"/></svg>
      </div>
      <h3>OUR SERVICES</h3>
      <p class="body-copy">Cloud based contact handling that lets us see every request clearly and respond quickly in any language our clients need.</p>
    </div>
    <div class="service sv2">
      <div class="icon" style="background:var(--green)">
        <svg width="24" height="18" viewBox="0 0 24 18" fill="none" stroke="#fff" stroke-width="2.4" stroke-linecap="round"><path d="M3 15a9 9 0 1 1 18 0"/><path d="M12 14l5-6"/></svg>
      </div>
      <h3>OUR SERVICES</h3>
      <p class="body-copy">Training in our customer care college gives agents the speed and skill to solve problems at the first contact with ease.</p>
    </div>
    <div class="service sv3">
      <div class="icon" style="background:var(--orange)">
        <svg width="22" height="22" viewBox="0 0 22 22" fill="#fff"><path d="M3 9l6-6 3 3a2.5 2.5 0 1 1 3 3l3 3-6 6-3-3a2.5 2.5 0 1 0-3-3z"/></svg>
      </div>
      <h3>OUR SERVICES</h3>
      <p class="body-copy">Passionate people and good technology together create service that clients remember and customers love to return to.</p>
    </div>
    <div class="brand"><span class="dot"></span>meadowlark</div>
    <span class="page-no">2</span>
  </section>

  <section class="slide s6">
    <h2 class="slide-title">BULLET TEXT</h2><div class="rule"></div>
    <ul class="bullets body-copy">
      <li>We serve clients in eighteen languages from Antwerp in Belgium and Fez in Morocco, together with our partner Vellorix. Our cloud platform links every centre, so calls, emails and chats flow to the right agent at the right moment with no delay for customers.</li>
      <li>In our customer care college we invest in training and coaching for every agent. When technology is good and people have strong knowledge, passion will come, and that passion is what sets our service apart from the rest.</li>
    </ul>
    <div class="brand"><span class="dot"></span>meadowlark</div>
    <span class="page-no">2</span>
  </section>

</main>
</body>
</html>
```